Kestrelbay Racquet Club app

Design a sporting app that can, post news, post events, capture and show live scores, link at least 6 websites, other functions would be an advantage. Real tennis is also known as Royal tennis and Court tennis.
This would be like a sporting clubs app that gives live scores.

Colors

Designer to choose colors to be used in the design.

Requirements
Must have
• post news, post events, capture and show live scores, link at least 6 websites,
Nice to have
• Instructions on how to launch the app on apple and android

```html
<!DOCTYPE html>
<html lang="en">
<head>
<meta charset="utf-8">
<title>Kestrelbay Racquet Club – App Screens</title>
<link href="https://fonts.googleapis.com/css2?family=Poppins:wght@400;500;600&display=swap" rel="stylesheet">
<style>
  :root {
    --stage: #0a92fe;
    --white: #ffffff;
    --screen-grey: #f2f2f3;
    --ink: #2b2b2b;
    --muted: #8a8a8a;
    --brand: #1d44f0;
    --brand-dark: #1530b8;
    --card-shadow: 0 4px 14px rgba(0,0,0,0.06);
  }
  * { box-sizing: border-box; margin: 0; padding: 0; }
  html, body { width: 1200px; height: 1109px; overflow: hidden; }
  body {
    background: var(--stage);
    font-family: "Poppins", sans-serif;
    position: relative;
    color: var(--ink);
  }
  .screen-title {
    position: absolute; top: 76px;
    font-size: 42px; font-weight: 600; color: var(--white);
    transform: translateX(-50%); white-space: nowrap;
  }
  .screen-title.start { left: 369px; }
  .screen-title.home { left: 884px; }

  .phone {
    position: absolute; top: 176px; width: 452px; height: 823px;
    border-radius: 36px; overflow: hidden;
  }
  .phone.start { left: 146px; background: var(--white); }
  .phone.home { left: 681px; width: 450px; background: var(--screen-grey); }

  .status-bar {
    position: absolute; top: 0; left: 0; right: 0; height: 26px;
    font-size: 16px; color: #111;
  }
  .status-bar .signal { position: absolute; left: 19px; top: 8px; }
  .status-bar .time { position: absolute; left: 50%; top: 2px; transform: translateX(-50%); font-weight: 500; }
  .status-bar .bt { position: absolute; right: 112px; top: 4px; }
  .status-bar .battery-level { position: absolute; right: 62px; top: 2px; }
  .status-bar .battery { position: absolute; right: 24px; top: 6px; }

  /* Start screen */
  .brand-mark {
    position: absolute; left: 50%; top: 180px; transform: translateX(-50%);
    width: 92px; height: 92px; border-radius: 50%; background: var(--brand);
  }
  .brand-name {
    position: absolute; left: 0; right: 0; top: 316px; text-align: center;
    font-size: 38px; font-weight: 600; color: var(--brand); letter-spacing: 1px;
  }
  .brand-tagline {
    position: absolute; left: 0; right: 0; top: 364px; text-align: center;
    font-size: 18px; color: var(--muted);
  }
  .get-start {
    position: absolute; left: 29px; top: 706px; width: 389px; height: 60px;
    border: 2px solid var(--brand); border-radius: 30px;
    display: flex; align-items: center; justify-content: center;
    font-size: 29px; font-weight: 500; color: var(--brand);
  }

  /* Home screen */
  .section-heading {
    position: absolute; left: 30px; font-size: 22px; font-weight: 500; color: var(--ink);
  }
  .score-card {
    position: absolute; left: 30px; top: 116px; width: 390px; height: 131px;
    background: var(--white); border-radius: 10px; box-shadow: var(--card-shadow);
  }
  .player { position: absolute; top: 26px; width: 110px; text-align: center; }
  .player.home-side { left: 6px; }
  .player.away-side { left: 274px; }
  .player .avatar {
    width: 62px; height: 62px; border-radius: 50%; margin: 0 auto;
  }
  .player.home-side .avatar { background: radial-gradient(circle at 50% 45%, #b98a6e, #2a3f8f 70%); }
  .player.away-side .avatar { background: radial-gradient(circle at 50% 45%, #d9a070, #2c8a3c 72%); }
  .player .name { margin-top: 8px; font-size: 11px; font-weight: 500; color: var(--ink); }
  .versus { position: absolute; left: 175px; top: 35px; width: 70px; text-align: center; }
  .versus svg { display: block; margin: 0 auto; }
  .versus .score { margin-top: 8px; font-size: 20px; font-weight: 600; letter-spacing: 2px; }
  .versus .score .trail { color: #b5b5b5; }
  .versus .score .sep { color: var(--brand); font-size: 16px; }
  .versus .score .lead { color: var(--brand); }

  .news-card {
    position: absolute; left: 30px; top: 344px; width: 360px; height: 118px;
    background: var(--white); border-radius: 10px; overflow: hidden; box-shadow: var(--card-shadow);
  }
  .news-card .photo {
    position: absolute; left: 0; top: 0; width: 124px; height: 118px;
    background: linear-gradient(160deg, #2c4f9c 0%, #1d2d4d 55%, #272a2c 100%);
  }
  .news-card .title {
    position: absolute; left: 147px; top: 14px; font-size: 18px; font-weight: 500; color: var(--ink);
  }
  .news-card .summary {
    position: absolute; left: 147px; top: 42px; width: 200px;
    font-size: 10.5px; line-height: 14.5px; color: #7a7a7a;
  }
  .news-card.next { left: 420px; width: 60px; }
  .news-card.next .photo { width: 60px; background: linear-gradient(160deg, #1a1d2a, #3a4f86 60%, #c9d3e6); }

  .event-card {
    position: absolute; top: 551px; width: 144px; height: 179px;
    border-radius: 18px; overflow: hidden; color: var(--white);
    box-shadow: 0 6px 14px rgba(0,0,0,0.15);
  }
  .event-card.one { left: 31px; background: linear-gradient(180deg, #5b3a52 0%, #a5524a 30%, #4a4f66 60%, #2e5a86 100%); }
  .event-card.two { left: 196px; background: linear-gradient(180deg, #1c2431 0%, #273241 50%, #b3202a 85%, #8d1a22 100%); }
  .event-card.three { left: 360px; background: linear-gradient(180deg, #777a80 0%, #3b4e6e 35%, #b3323a 75%, #2a7ac2 100%); }
  .event-card .heart { position: absolute; left: 98px; top: 20px; }
  .event-card .headline {
    position: absolute; left: 20px; top: 60px; width: 126px;
    font-size: 17.5px; line-height: 21px; font-weight: 500; white-space: nowrap;
  }
  .event-card .date {
    position: absolute; left: 20px; top: 110px; font-size: 11px;
    display: flex; align-items: center; gap: 3px; white-space: nowrap;
  }
</style>
</head>
<body>

<h1 class="screen-title start">Star Page</h1>
<h1 class="screen-title home">Home Page</h1>

<section class="phone start">
  <div class="status-bar">
    <svg class="signal" width="68" height="10" viewBox="0 0 68 10">
      <circle cx="5" cy="5" r="4" fill="#111"/><circle cx="15" cy="5" r="4" fill="#111"/><circle cx="25" cy="5" r="4" fill="#111"/>
      <circle cx="35" cy="5" r="3.4" fill="none" stroke="#111" stroke-width="1"/><circle cx="45" cy="5" r="3.4" fill="none" stroke="#111" stroke-width="1"/>
      <path d="M54 3.5 a8 8 0 0 1 12 0 M56.2 5.8 a5 5 0 0 1 7.6 0" fill="none" stroke="#111" stroke-width="1.6"/>
      <circle cx="60" cy="8.4" r="1.4" fill="#111"/>
    </svg>
    <span class="time">4:21 PM</span>
    <svg class="bt" width="10" height="16" viewBox="0 0 10 16"><path d="M1 4 L8 11 L5 14 V2 L8 5 L1 12" fill="none" stroke="#888" stroke-width="1.2"/></svg>
    <span class="battery-level">100%</span>
    <svg class="battery" width="34" height="13" viewBox="0 0 34 13"><rect x="0.5" y="0.5" width="30" height="12" rx="2" fill="#111" stroke="#111"/><rect x="31" y="4" width="2.5" height="5" rx="1" fill="#111"/></svg>
  </div>

  <div class="brand-mark"></div>
  <div class="brand-name">Kestrelbay</div>
  <div class="brand-tagline">Real Tennis App</div>

  <div class="get-start">Get Start</div>
</section>

<section class="phone home">
  <div class="status-bar">
    <svg class="signal" width="68" height="10" viewBox="0 0 68 10">
      <circle cx="5" cy="5" r="4" fill="#111"/><circle cx="15" cy="5" r="4" fill="#111"/><circle cx="25" cy="5" r="4" fill="#111"/>
      <circle cx="35" cy="5" r="3.4" fill="none" stroke="#111" stroke-width="1"/><circle cx="45" cy="5" r="3.4" fill="none" stroke="#111" stroke-width="1"/>
      <path d="M54 3.5 a8 8 0 0 1 12 0 M56.2 5.8 a5 5 0 0 1 7.6 0" fill="none" stroke="#111" stroke-width="1.6"/>
      <circle cx="60" cy="8.4" r="1.4" fill="#111"/>
    </svg>
    <span class="time">4:21 PM</span>
    <svg class="bt" width="10" height="16" viewBox="0 0 10 16"><path d="M1 4 L8 11 L5 14 V2 L8 5 L1 12" fill="none" stroke="#888" stroke-width="1.2"/></svg>
    <span class="battery-level">100%</span>
    <svg class="battery" width="34" height="13" viewBox="0 0 34 13"><rect x="0.5" y="0.5" width="30" height="12" rx="2" fill="#111" stroke="#111"/><rect x="31" y="4" width="2.5" height="5" rx="1" fill="#111"/></svg>
  </div>

  <h2 class="section-heading" style="top:68px">Live Score</h2>
  <div class="score-card">
    <div class="player home-side">
      <div class="avatar" role="img" aria-label="Portrait photo of player Lucas Marven"></div>
      <div class="name">Lucas Marven</div>
    </div>
    <div class="versus">
      <svg width="44" height="44" viewBox="0 0 44 44">
        <circle cx="22" cy="22" r="20" fill="none" stroke="#dfe3f5" stroke-width="2"/>
        <path d="M22 2 A20 20 0 1 1 6 10" fill="none" stroke="var(--brand)" stroke-width="2.4" stroke-linecap="round"/>
        <text x="22" y="27" text-anchor="middle" font-family="Poppins, sans-serif" font-size="13" font-weight="600" fill="#333">VS</text>
      </svg>
      <div class="score"><span class="trail">2</span> <span class="sep">:</span> <span class="lead">4</span></div>
    </div>
    <div class="player away-side">
      <div class="avatar" role="img" aria-label="Portrait photo of player Diego Santal"></div>
      <div class="name">Diego Santal</div>
    </div>
  </div>

  <h2 class="section-heading" style="top:274px">Trending News</h2>
  <article class="news-card">
    <div class="photo" role="img" aria-label="Photo of a tennis player celebrating on court"></div>
    <h3 class="title">Tennis News Title</h3>
    <p class="summary">Lorem ipsum dolor sit amet, consectetur adipisicing elit, sed do eiusmod tempor incididunt ..</p>
  </article>
  <article class="news-card next">
    <div class="photo" role="img" aria-label="Photo for the next news story"></div>
  </article>

  <h2 class="section-heading" style="top:484px; left:31px">Upcoming Events</h2>

  <article class="event-card one" role="img" aria-label="Photo of a tennis stadium at sunset">
    <svg class="heart" width="24" height="22" viewBox="0 0 24 22"><path d="M12 20 C5 14 1.5 10.5 1.5 6.5 A5 5 0 0 1 12 4.5 A5 5 0 0 1 22.5 6.5 C22.5 10.5 19 14 12 20 Z" fill="none" stroke="#fff" stroke-width="1.6"/></svg>
    <div class="headline">Elite Tour<br>in 2020</div>
    <div class="date"><svg width="11" height="11" viewBox="0 0 12 12"><circle cx="6" cy="6" r="5" fill="none" stroke="#fff" stroke-width="1.3"/><path d="M6 3 V6 H8.5" fill="none" stroke="#fff" stroke-width="1.3"/></svg>15 Feb 2020</div>
  </article>
  <article class="event-card two" role="img" aria-label="Photo of a player holding a racquet">
    <svg class="heart" width="24" height="22" viewBox="0 0 24 22"><path d="M12 20 C5 14 1.5 10.5 1.5 6.5 A5 5 0 0 1 12 4.5 A5 5 0 0 1 22.5 6.5 C22.5 10.5 19 14 12 20 Z" fill="none" stroke="#fff" stroke-width="1.6"/></svg>
    <div class="headline">Milan will<br>play a new...</div>
    <div class="date"><svg width="11" height="11" viewBox="0 0 12 12"><circle cx="6" cy="6" r="5" fill="none" stroke="#fff" stroke-width="1.3"/><path d="M6 3 V6 H8.5" fill="none" stroke="#fff" stroke-width="1.3"/></svg>15 Feb 2020</div>
  </article>
  <article class="event-card three" role="img" aria-label="Photo of a crowded tennis arena">
    <div class="headline">Tokyo Open<br>Event 2020</div>
    <div class="date"><svg width="11" height="11" viewBox="0 0 12 12"><circle cx="6" cy="6" r="5" fill="none" stroke="#fff" stroke-width="1.3"/><path d="M6 3 V6 H8.5" fill="none" stroke="#fff" stroke-width="1.3"/></svg>15 Feb 2020</div>
  </article>
</section>

</body>
</html>
```